Seven nights at the harbour

Creation of the cover for the book: "Sept nuits sur le quai du port" with the joined photo of a 70 years old lady.
Title: "Seven nights along the old harbour"
Author: "Mireille Vaston"
Publisher: "Editions Morvane" (should be at the bottom of the page)
Format: 14 x 20.5 cm
The story: A senior lady (70 years old), divorced, with a beautiful face, still wants to seduce, even young men.
We found the perfect photo for the woman. We would like to ask you to make a modern cover from it.
Besoin de quelques jours pour choisir un design
Target Market(s)
Novels reader (adults)
Industry/Entity Type
book

```html
<!DOCTYPE html>
<html lang="fr">
<head>
<meta charset="utf-8">
<title>Sept nuits sur le quai du port — couverture</title>
<link rel="stylesheet" href="https://fonts.googleapis.com/css2?family=Allura&family=Cormorant+Garamond:wght@500;600&family=EB+Garamond&display=swap">
<style>
  :root {
    --cover-slate: #4f5c5a;
    --ink-white: #ffffff;
    --author-pink: #e9a5a5;
    --hair-light: #e4e6e6;
    --hair-mid: #a9adae;
    --hair-dark: #5d6263;
    --skin: #d9a08f;
  }
  html, body { margin: 0; padding: 0; overflow: hidden; }
  body { width: 1200px; height: 830px; background: var(--cover-slate); }
  .cover {
    position: relative; width: 1200px; height: 830px;
    background: var(--cover-slate); overflow: hidden;
    color: var(--ink-white);
  }

  .script { font-family: "Allura", cursive; font-weight: 400; }
  .caps-serif { font-family: "Cormorant Garamond", serif; font-weight: 500; text-transform: uppercase; }

  /* back cover */
  .back-title { position: absolute; left: 70px; width: 418px; top: 78px; text-align: center; line-height: 1; }
  .back-title .line-script { font-size: 40px; }
  .back-title .line-small { font-size: 20px; margin-top: -8px; }
  .back-title .line-caps { font-size: 37px; margin-top: -4px; letter-spacing: 0.5px; }
  .blurb {
    position: absolute; left: 70px; top: 212px; width: 418px; margin: 0;
    font-family: "EB Garamond", serif; font-size: 12.6px; line-height: 17px;
    text-align: justify; text-align-last: center; hyphens: auto;
  }
  .isbn-box { position: absolute; left: 70px; top: 698px; width: 124px; height: 83px; background: var(--ink-white); }
  .publisher-back { position: absolute; left: 214px; top: 760px; font-size: 19px; letter-spacing: 0.3px; }

  /* spine */
  .spine-title {
    position: absolute; left: 392px; top: 208px; width: 420px; height: 60px;
    transform: rotate(-90deg); transform-origin: center;
    display: flex; align-items: center; justify-content: center; gap: 8px; white-space: nowrap;
  }
  .spine-title .line-script { font-size: 34px; }
  .spine-title .line-small { font-size: 20px; }
  .spine-title .line-caps { font-size: 28px; }
  .spine-author {
    position: absolute; left: 478px; top: 586px; width: 252px; height: 24px;
    transform: rotate(-90deg); transform-origin: center; text-align: center;
    color: var(--author-pink); font-size: 16px; letter-spacing: 7px; line-height: 24px; white-space: nowrap;
  }
  .spine-mark { position: absolute; left: 579px; top: 757px; width: 53px; height: 53px; border-radius: 50%; background: var(--ink-white); }

  /* front cover */
  .front-author {
    position: absolute; left: 660px; width: 540px; top: 24px; text-align: center;
    color: var(--author-pink); font-size: 31px; letter-spacing: 10px;
  }
  .portrait { position: absolute; left: 674px; top: 74px; width: 492px; height: 492px; }
  .front-title { position: absolute; left: 660px; width: 540px; top: 572px; text-align: center; line-height: 1; }
  .front-title .line-script { font-size: 66px; }
  .front-title .line-small { font-size: 30px; margin-top: -14px; }
  .front-title .line-caps { font-size: 66px; margin-top: -8px; letter-spacing: 1px; }
  .publisher-front { position: absolute; left: 660px; width: 540px; top: 771px; text-align: center; font-size: 20px; letter-spacing: 0.3px; }
</style>
</head>
<body>
<div class="cover">

  <section class="back-cover">
    <div class="back-title">
      <div class="line-script script">Sept nuits sur le quai</div>
      <div class="line-small script">du</div>
      <div class="line-caps caps-serif">Port</div>
    </div>
    <p class="blurb">Lorem ipsum dolor sit amet, consectetur adipiscing elit. Etiam nisi diam, convallis at dictum in, dapibus sit amet mi. Praesent rutrum lacus magna, eget molestie velit lobortis non. Etiam sollicitudin tristique massa at sodales. Duis faucibus egestas odio pretium facilisis. Etiam scelerisque in mauris sed interdum. Nullam diam turpis, sodales ut feugiat in, suscipit in erat. Nullam et risus egestas, porta elit vel, semper lacus. Cras pretium consequat vestibulum. In id sapien ut ex blandit suscipit a sit amet mauris. Ut pharetra gravida tempus. Sed ornare quam sed quam convallis, bibendum pulvinar magna sollicitudin. Duis vel tempor enim. Nulla sit amet urna ac ex pretium ullamcorper.</p>
    <div class="isbn-box" aria-hidden="true"></div>
    <div class="publisher-back caps-serif">Editions Morvane</div>
  </section>

  <section class="spine">
    <div class="spine-title">
      <span class="line-script script">Sept nuits sur le quai</span>
      <span class="line-small script">du</span>
      <span class="line-caps caps-serif">Port</span>
    </div>
    <div class="spine-author caps-serif">Mireille Vaston</div>
    <div class="spine-mark" aria-hidden="true"></div>
  </section>

  <section class="front-cover">
    <div class="front-author caps-serif">Mireille Vaston</div>
    <svg class="portrait" viewBox="0 0 492 492" role="img" aria-label="Photo of a seventy-year-old woman with windswept silver hair covering her face">
      <defs>
        <radialGradient id="hair-tone" cx="45%" cy="40%" r="65%">
          <stop offset="0%" stop-color="var(--hair-light)"/>
          <stop offset="45%" stop-color="var(--hair-mid)"/>
          <stop offset="85%" stop-color="var(--hair-light)"/>
          <stop offset="100%" stop-color="var(--hair-dark)"/>
        </radialGradient>
      </defs>
      <circle cx="246" cy="246" r="246" fill="url(#hair-tone)"/>
    </svg>
    <div class="front-title">
      <div class="line-script script">Sept nuits sur le quai</div>
      <div class="line-small script">du</div>
      <div class="line-caps caps-serif">Port</div>
    </div>
    <div class="publisher-front caps-serif">Editions Morvane</div>
  </section>

</div>
</body>
</html>
```